Medical Office Needs an Updated Treatment Brochure

We need an updated brochure for a new treatment our offices are offering. The old brochure attached has all the current information on it, it just needs a new design.
We would like the updated version to be more modern and sleek as well as engaging.
Please see the old brochure attached for reference as well as this link: http://www.velmirova.com/medspa/iv-therapy/#1
The content from the attached brochure will remain.
UPDATE**** PLEASE SEE THE ATTACHED EXAMPLE BROCHURE OF THE DESIGN WE ARE LOOKING FOR!!
Thank you!!

```html
<!DOCTYPE html>
<html lang="en">
<head>
<meta charset="utf-8">
<title>Velmirova – IV Nutrient Therapy Brochure</title>
<link rel="stylesheet" href="https://fonts.googleapis.com/css2?family=Lora:wght@400;700&family=Open+Sans:wght@400;600&family=Oswald:wght@500&display=swap">
<style>
  :root {
    --page-bg: #e4e4e4;
    --paper: #ffffff;
    --pink: #d9607e;
    --pink-soft: #ecb8c6;
    --green: #8ccb8e;
    --green-deep: #6fb273;
    --charcoal: #3f3f41;
    --charcoal-light: #6a6a6d;
    --ink: #2f2f31;
    --text: #3c3c3c;
  }
  * { box-sizing: border-box; margin: 0; padding: 0; }
  html, body { width: 1200px; height: 1005px; overflow: hidden; }
  body {
    background: var(--page-bg);
    font-family: "Open Sans", sans-serif;
    color: var(--text);
    position: relative;
  }
  .brochure {
    position: absolute; left: 45px; top: 73px;
    width: 1110px; height: 858px;
    display: flex;
    box-shadow: 0 10px 30px rgba(0,0,0,.18);
  }
  .panel { position: relative; width: 370px; height: 858px; overflow: hidden; background: var(--paper); }
  .panel svg.backdrop { position: absolute; inset: 0; }
  .brand-name {
    font-family: "Lora", serif; font-weight: 400; color: var(--green-deep);
    display: flex; align-items: center; gap: 8px;
  }
  .brand-dot { width: 12px; height: 12px; border-radius: 50%; background: var(--pink-soft); }

  /* Left panel */
  .team-photo { position: absolute; left: 0; top: 0; width: 370px; height: 350px; }
  .intro-heading {
    position: absolute; left: 34px; top: 400px;
    font-family: "Lora", serif; font-size: 26px; color: var(--pink);
  }
  .intro-copy {
    position: absolute; left: 34px; top: 446px; width: 306px;
    font-size: 12px; line-height: 1.5;
  }
  .intro-copy p + p { margin-top: 10px; }
  .intro-tagline {
    position: absolute; left: 20px; top: 600px; width: 330px; text-align: center;
    font-family: "Lora", serif; color: var(--pink); line-height: 1.25;
  }
  .intro-tagline .big { font-size: 28px; display: block; }
  .intro-tagline .small { font-size: 21px; display: block; }
  .left-brand { position: absolute; left: 60px; top: 706px; font-size: 46px; }
  .bottom-band { position: absolute; left: 0; bottom: 0; width: 370px; height: 46px; background: var(--charcoal); }

  /* Middle panel */
  .about-title {
    position: absolute; left: 0; top: 80px; width: 370px; text-align: center;
    font-family: "Open Sans", sans-serif; font-weight: 600; font-size: 24px; letter-spacing: 1px; color: #fff;
  }
  .about-copy {
    position: absolute; left: 36px; top: 130px; width: 298px;
    font-size: 11.5px; line-height: 1.55; color: #f1f1f1; text-align: center;
  }
  .about-copy p + p { margin-top: 12px; }
  .mid-brand { position: absolute; left: 46px; top: 500px; font-size: 30px; color: var(--charcoal); }
  .contact {
    position: absolute; left: 110px; top: 600px; width: 250px; text-align: center;
    color: #fff; font-size: 12px; line-height: 1.45;
  }
  .contact .office-name { color: var(--pink); font-weight: 600; font-family: "Lora", serif; font-size: 13px; }
  .contact hr { border: none; border-top: 1px solid var(--charcoal); margin: 6px 20px; }
  .contact .email { color: var(--ink); margin-top: 14px; font-size: 12.5px; }
  .web {
    font-family: "Open Sans", sans-serif; font-weight: 600; color: var(--ink);
    letter-spacing: 3px;
  }
  .contact .web { margin-top: 8px; font-size: 14px; }

  /* Cover panel */
  .cover-brand { position: absolute; left: 0; top: 36px; width: 370px; justify-content: center; font-size: 40px; }
  .cover-photo { position: absolute; left: 30px; top: 110px; }
  .cover-title {
    position: absolute; left: 0; top: 500px; width: 370px; text-align: center;
    font-family: "Lora", serif; font-weight: 700; color: var(--ink); line-height: 1.05;
  }
  .cover-title .line1 { font-size: 38px; display: block; }
  .cover-title .line2 { font-size: 50px; display: block; }
  .cover-subtitle {
    position: absolute; left: 0; top: 640px; width: 370px; text-align: center;
    font-family: "Oswald", sans-serif; font-weight: 500; font-size: 25px; line-height: 1.25; color: #fff;
  }
  .cover-web { position: absolute; left: 0; top: 760px; width: 370px; text-align: center; font-size: 15px; }
</style>
</head>
<body>
<main class="brochure">

  <section class="panel panel-intro">
    <svg class="backdrop" width="370" height="858" viewBox="0 0 370 858">
      <rect class="team-photo" width="370" height="350" fill="#e9ecf0" role="img" aria-label="Photo of the smiling medical team in scrubs and white coat"/>
      <path d="M0 210 C60 300 180 345 370 340 V370 H0 Z" fill="var(--paper)"/>
      <path d="M0 210 C60 300 180 345 370 340 V352 C170 362 50 320 0 250 Z" fill="var(--pink-soft)"/>
      <path d="M0 250 C50 320 170 362 370 352 V358 C160 372 40 330 0 262 Z" fill="var(--charcoal-light)"/>
    </svg>
    <h2 class="intro-heading">What is IV Therapy?</h2>
    <div class="intro-copy">
      <p>IV Nutrient Therapy involves the direct administration of vital minerals, nutrients and vitamins directly into the bloodstream (intravenously infused) through an IV drip.</p>
      <p>These essential nutrients can help boost immune function, increase energy levels, assist in weight management, avoid chronic health issues, and even aid in skin rejuvenation.</p>
    </div>
    <p class="intro-tagline"><span class="big">IV Therapy is great for</span><span class="small">boosting health and preventing illness</span></p>
    <div class="brand-name left-brand">Velmirova<span class="brand-dot"></span></div>
    <div class="bottom-band"></div>
  </section>

  <section class="panel panel-about">
    <svg class="backdrop" width="370" height="858" viewBox="0 0 370 858">
      <defs>
        <linearGradient id="aboutGrad" x1="0" y1="0" x2="0" y2="1">
          <stop offset="0" stop-color="#5a5a5d"/>
          <stop offset="1" stop-color="var(--charcoal)"/>
        </linearGradient>
      </defs>
      <path d="M0 0 H370 V500 L0 440 Z" fill="url(#aboutGrad)"/>
      <path d="M0 440 L370 500 V545 C170 600 50 720 0 858 Z" fill="var(--pink-soft)"/>
      <path d="M0 858 C50 720 170 600 370 545 V858 Z" fill="var(--green)"/>
    </svg>
    <h2 class="about-title">ABOUT US :</h2>
    <div class="about-copy">
      <p>Velmirova is the region's trusted home for cosmetic surgery and medical aesthetics, offering patients a calm setting, skilled providers and modern treatments, from injectables and fillers to laser care and advanced skin therapies.</p>
      <p>At Velmirova, we are dedicated to helping every patient look and feel their best. Our surgeons, nurses and staff give personal attention at each visit, and we remain committed to safe, thoughtful care and beautiful, natural results.</p>
    </div>
    <div class="brand-name mid-brand">Velmirova</div>
    <address class="contact" style="font-style:normal">
      <div class="office-name">Velmirova</div>
      <div>Velmirova 2210 Harbor Lane<br>Larkfield CA 90120</div>
      <hr>
      <div class="office-name">Velmirova Southwest</div>
      <div>Velmirova Southwest 815 Alder Road,<br>Suite 300 Larkfield, CA 90124</div>
      <div class="email">E Mail: care@velmirova.com</div>
      <div class="web">www.velmirova.com</div>
    </address>
  </section>

  <section class="panel panel-cover">
    <svg class="backdrop" width="370" height="858" viewBox="0 0 370 858">
      <path d="M0 480 C150 480 280 420 370 330 V858 H0 Z" fill="var(--green)"/>
    </svg>
    <div class="brand-name cover-brand">Velmirova<span class="brand-dot"></span></div>
    <svg class="cover-photo" width="310" height="310" viewBox="0 0 310 310">
      <defs>
        <radialGradient id="dripGrad" cx="0.4" cy="0.55" r="0.6">
          <stop offset="0" stop-color="#c9b7e6"/>
          <stop offset="0.5" stop-color="#7fa6c9"/>
          <stop offset="1" stop-color="#3f6b86"/>
        </radialGradient>
      </defs>
      <circle cx="155" cy="155" r="148" fill="url(#dripGrad)" role="img" aria-label="Close-up photo of an IV drip chamber with soft bokeh lights"/>
      <circle cx="155" cy="155" r="148" fill="none" stroke="var(--pink)" stroke-width="7"/>
    </svg>
    <h1 class="cover-title"><span class="line1">IV NUTRIENT</span><span class="line2">THERAPY</span></h1>
    <p class="cover-subtitle">REVITALIZE, RECHARGE<br>&amp; REJUVENTAL</p>
    <div class="web cover-web">www.velmirova.com</div>
  </section>

</main>
</body>
</html>
```